4D Hush Little Nest Luxury Ultrasound Billboard

Design a HIGH-END, MODERN billboard for my private prenatal ultrasound studio, 4D Hush Little Nest, located in Pace, Florida.
This billboard will be viewed by drivers traveling at highway speeds, so it must be extremely clean, simple, and readable within 6 seconds.
About My Business
4D Hush Little Nest is a private prenatal ultrasound studio specializing in:
Highest technology 4D/HD Ultrasounds
Early Gender Determination
Pregnancy Confirmation
I have been serving families for nearly 10 years and is known for creating a memorable experience, not just an ultrasound appointment.
Design Style
I DO NOT want:
Flowers
Leaves
Swirls
Glitter
Hearts everywhere
Busy backgrounds
Generic maternity stock graphics
I DO want:
Modern
Luxury
Upscale
Clean
Professional
Eye-catching
Premium medical spa feel
Colors
Use colors from my logo:
LOGO Green ( or a deep green)
Black
White
Soft Gold accents
Images:
Incorporate my professional headshot in a clean, modern way, logo, and the ultrasound images
Text
Keep wording minimal.
Primary Headline ( OPEN TO IDEAS) :
EXAMPLES ( WOULD RATHER SOMETHING MORE CATCHY)
" ADVANCED IMAGING. UNFORGETTABLE MOMENTS"
"MEET YOUR BABY BEFORE BIRTH"
Under headline:
4D Ultrasound • Early Gender • Pregnancy Confirmation
Business Name:
4D Hush Little Nest
Private Prenatal Ultrasound Studio
Phone Number:
850-471-3905
Important
This billboard must be readable in 5–6 seconds from a moving vehicle.
Less text is better.
The phone number and business name must be visible from a distance.
The design should feel like a premium brand that immediately tells expecting parents:
“This is where I go to see my baby.”
Files Provided
Official logo
Headshot
Ultrasound images
Don’t make this look like a medical office billboard.
Make it look like a luxury baby experience billboard. That’s what separates 4D Hush Little Nest from hospitals, OB offices, and all the new studios popping up around you. The emotional connection is what gets moms to book. ❤️
Billboard Size - 10.6” x 36”

```html
<!DOCTYPE html>
<html lang="en">
<head>
<meta charset="utf-8">
<title>4D Hush Little Nest – Billboard</title>
<link rel="stylesheet" href="https://fonts.googleapis.com/css2?family=Poppins:wght@500;600;700;800&display=swap">
<style>
  :root {
    --stage: #4b4849;
    --ink: #0b0b0b;
    --white: #ffffff;
    --panel-light: #fbfbfb;
    --panel-grey: #d9d9d9;
    --gold: #c9a03d;
    --logo-green: #4f5d58;
    --frame-grey: #6d7471;
    --skin: #e8c9b0;
    --denim: #5a7fa8;
    --scrub-green: #2f4a37;
    --scan-brown: #7a3f2c;
  }
  * { margin: 0; padding: 0; box-sizing: border-box; }
  html, body {
    width: 1129px; height: 1200px; overflow: hidden;
    background: var(--stage);
    font-family: "Poppins", Arial, sans-serif;
  }
  .billboard {
    position: absolute; left: 40px; top: 445px;
    width: 1049px; height: 309px; overflow: hidden;
    background: linear-gradient(90deg, var(--white) 0%, var(--panel-light) 35%, var(--panel-grey) 100%);
  }
  .headshot {
    position: absolute; left: 0; top: 0; width: 190px; height: 100%;
    background: linear-gradient(180deg, #e9dcc6 0%, #d8c3a1 30%, var(--scrub-green) 62%, #24382a 100%);
    -webkit-mask-image: linear-gradient(90deg, #000 78%, transparent 100%);
    mask-image: linear-gradient(90deg, #000 78%, transparent 100%);
  }
  .belly-photo {
    position: absolute; right: 0; top: 0; width: 326px; height: 100%;
    background: linear-gradient(180deg, #f4f4f4 0%, #f4f4f4 14%, var(--skin) 22%, #e2bea3 70%, var(--denim) 82%, #47698f 100%);
    -webkit-mask-image: linear-gradient(90deg, transparent 0%, #000 14%);
    mask-image: linear-gradient(90deg, transparent 0%, #000 14%);
  }
  .footer-band {
    position: absolute; left: 186px; right: 0; bottom: 0; height: 50px;
    background: var(--white);
  }
  .headline {
    position: absolute; left: 192px; top: 18px;
    font-weight: 800; font-size: 55px; line-height: 0.92;
    color: var(--ink); letter-spacing: 0.5px;
  }
  .brand-box {
    position: absolute; left: 198px; top: 142px; width: 198px; height: 98px;
    border: 2px solid var(--frame-grey); border-radius: 12px;
    background: var(--white);
    display: flex; flex-direction: column; align-items: center; justify-content: center;
    text-align: center; gap: 6px;
  }
  .brand-name {
    font-weight: 700; font-size: 19px; line-height: 1.1; color: var(--gold);
  }
  .brand-rule { width: 160px; height: 1px; background: var(--gold); }
  .brand-tag {
    font-weight: 500; font-size: 8.5px; letter-spacing: 0.4px; color: var(--logo-green);
  }
  .services {
    position: absolute; left: 413px; top: 144px; list-style: none;
    font-weight: 600; font-size: 17px; line-height: 1.05; color: var(--ink);
  }
  .services li { display: flex; align-items: flex-start; gap: 5px; margin-bottom: 10px; }
  .services svg { flex: none; margin-top: 2px; }
  .scan-card {
    position: absolute; left: 607px; top: 70px; width: 182px; height: 182px;
    background: var(--white); padding: 11px 11px 30px;
    transform: rotate(-8deg);
    box-shadow: 0 3px 8px rgba(0,0,0,0.25);
  }
  .scan-image {
    width: 100%; height: 100%;
    background: radial-gradient(ellipse at 45% 45%, #d9987c 0%, #b06a4f 40%, var(--scan-brown) 70%, #3a1a12 100%);
  }
  .booking {
    position: absolute; left: 195px; bottom: 10px;
    display: flex; align-items: center;
  }
  .booking-cta { font-weight: 600; font-size: 14.5px; color: var(--ink); margin-right: 14px; }
  .booking-phone { font-weight: 700; font-size: 31px; color: var(--ink); margin-left: 8px; letter-spacing: 0.5px; }
</style>
</head>
<body>
  <main class="billboard">
    <div class="headshot" role="img" aria-label="Portrait of the studio owner in green scrubs holding an ultrasound probe"></div>
    <div class="belly-photo" role="img" aria-label="Pregnant belly covered with question-mark sticky notes"></div>
    <div class="footer-band"></div>

    <h1 class="headline">MEET YOUR BABY<br>BEFORE BIRTH</h1>

    <div class="brand-box">
      <div class="brand-name">4D Hush Little Nest</div>
      <div class="brand-rule"></div>
      <div class="brand-tag">PRENATAL ULTRASOUND STUDIO</div>
    </div>

    <ul class="services">
      <li><svg width="15" height="15" viewBox="0 0 16 16"><circle cx="8" cy="8" r="6.5" fill="none" stroke="#6d7471" stroke-width="1.6"/><path d="M4.5 8.2l2.4 2.4L13 4" fill="none" stroke="#c9a03d" stroke-width="2" stroke-linecap="round"/></svg>4D ULTRASOUND</li>
      <li><svg width="15" height="15" viewBox="0 0 16 16"><circle cx="8" cy="8" r="6.5" fill="none" stroke="#6d7471" stroke-width="1.6"/><path d="M4.5 8.2l2.4 2.4L13 4" fill="none" stroke="#c9a03d" stroke-width="2" stroke-linecap="round"/></svg>EARLY GENDER</li>
      <li><svg width="15" height="15" viewBox="0 0 16 16"><circle cx="8" cy="8" r="6.5" fill="none" stroke="#6d7471" stroke-width="1.6"/><path d="M4.5 8.2l2.4 2.4L13 4" fill="none" stroke="#c9a03d" stroke-width="2" stroke-linecap="round"/></svg>PREGNANCY<br>CONFIRMATION</li>
    </ul>

    <div class="scan-card">
      <div class="scan-image" role="img" aria-label="4D ultrasound image of twin babies"></div>
    </div>

    <div class="booking">
      <span class="booking-cta">BOOK YOUR APPOINTMENT NOW</span>
      <svg width="16" height="28" viewBox="0 0 16 28" aria-hidden="true"><rect x="1.5" y="1.5" width="13" height="25" rx="2.5" fill="none" stroke="#c9a03d" stroke-width="2.5"/><line x1="6" y1="23" x2="10" y2="23" stroke="#c9a03d" stroke-width="1.5"/></svg>
      <span class="booking-phone">850 471 3905</span>
    </div>
  </main>
</body>
</html>
```